Wine Label named: Amber Ridge

We are a wine producer, who wishes to launch a new premium wine called: Amber Ridge
Our winery is situated in a rolling hill, with slopes, where Amber Ridge exists in the property. One dates to the 15th century and the other more recent to the 18th century. Its a unique feature of the winery and we wish to create a label that represents these, but is NOT religious! Difficult task I know. Think you can pull it off? Let us see it! We start with one label, but the winner will have 5 more labels to design.

Target Market(s)

30-50 year old men

Industry/Entity Type

Wine

Colors

Designer to choose colors to be used in the design.

Requirements
Must have
• serious look and premium feel. name of the wine: Amber Ridge
Nice to have
• 2019 14% ABV
Should not have
• a religious look and feel

```html
<!DOCTYPE html>
<html lang="en">
<head>
<meta charset="utf-8">
<title>Amber Ridge – Wine Label</title>
<link href="https://fonts.googleapis.com/css2?family=Tulpen+One&display=swap" rel="stylesheet">
<style>
  :root {
    --page: #ffffff;
    --frame: #0e4b5c;
    --ink: #0d4556;
    --hill-top: #0b2f39;
    --hill-bottom: #02161b;
    --light: #ffffff;
  }
  html, body {
    margin: 0;
    padding: 0;
    width: 1200px;
    height: 1200px;
    overflow: hidden;
    background: var(--page);
    -webkit-font-smoothing: antialiased;
    -moz-osx-font-smoothing: grayscale;
  }
  .canvas {
    position: relative;
    width: 1200px;
    height: 1200px;
  }
  .label {
    position: absolute;
    left: 253px;
    top: 211px;
    width: 695px;
    height: 765px;
    border: 2px solid var(--frame);
    box-sizing: border-box;
    overflow: hidden;
    background: var(--page);
  }
  .hill-scene {
    position: absolute;
    left: 0;
    top: 0;
    width: 100%;
    height: 100%;
  }
  .wine-name {
    position: absolute;
    left: 0;
    right: 0;
    top: 131px;
    margin: 0;
    text-align: center;
    font-family: "Tulpen One", sans-serif;
    font-weight: 400;
    color: var(--ink);
    line-height: 1;
  }
  .wine-name span {
    display: block;
    font-size: 56px;
    letter-spacing: 20px;
    padding-left: 20px;
  }
  .wine-name span + span {
    margin-top: 18px;
  }
  .vintage,
  .abv {
    position: absolute;
    left: 0;
    right: 0;
    text-align: center;
    font-family: "Tulpen One", sans-serif;
    font-weight: 400;
    color: var(--light);
    line-height: 1;
    will-change: transform;
    text-shadow: none;
  }
  .vintage {
    top: 630px;
    font-size: 62px;
    letter-spacing: 14px;
    padding-left: 14px;
  }
  .abv {
    top: 720px;
    font-size: 22px;
    letter-spacing: 7px;
    padding-left: 7px;
  }
</style>
</head>
<body>
  <div class="canvas">
    <div class="label">
      <svg class="hill-scene" viewBox="0 0 695 765" role="img" aria-label="Photograph of two small whitewashed buildings standing on a dark rolling hilltop, toned in deep teal">
        <defs>
          <linearGradient id="hillShade" x1="0" y1="0" x2="0" y2="1">
            <stop offset="0" stop-color="#0b2f39"/>
            <stop offset="1" stop-color="#02161b"/>
          </linearGradient>
        </defs>
        <path d="M0 474 C 90 452, 200 440, 300 432 C 360 424, 400 420, 440 428 C 540 444, 620 460, 695 480 L 695 765 L 0 765 Z" fill="url(#hillShade)"/>
      </svg>
      <h1 class="wine-name"><span>AMBER</span><span>RIDGE</span></h1>
      <div class="vintage">2019</div>
      <div class="abv">14% ABV</div>
    </div>
  </div>
</body>
</html>
```